Commercial Construction Company

We need a business card design based on our current logo. We are a commercial general contractor based in Southern California that specializes in bank remodels. We would like to see designs that incorporate dark blue. The final design should portray an image of professionalism and quality.

If possible, I would like to add metallic foil to the design. Thank you

```html
<!DOCTYPE html>
<html lang="en">
<head>
<meta charset="utf-8">
<title>HBG Construction Services – Business Card</title>
<link href="https://fonts.googleapis.com/css2?family=Libre+Baskerville:wght@400;700&display=swap" rel="stylesheet">
<style>
  :root {
    --backdrop: #ece8e3;
    --card-front: #161616;
    --card-back: #063533;
    --foil: #c9a862;
    --foil-soft: #b39455;
    --card-shadow: rgba(0,0,0,0.22);
  }
  * { margin: 0; padding: 0; box-sizing: border-box; }
  html, body {
    width: 1200px; height: 1041px; overflow: hidden;
    background: var(--backdrop);
    font-family: "Libre Baskerville", Georgia, serif;
    color: var(--foil);
  }
  .canvas {
    position: relative; width: 1200px; height: 1041px;
    display: flex; flex-direction: column; align-items: center; justify-content: center; gap: 60px;
  }
  .card {
    position: relative; width: 600px; height: 343px;
    box-shadow: 0 14px 34px var(--card-shadow);
  }
  /* Front */
  .card--front { background: var(--card-front); }
  .card__frame {
    position: absolute; inset: 12px;
    border: 1px solid var(--foil-soft);
  }
  .front__mark {
    position: absolute; left: 0; right: 0; top: 98px;
    display: flex; align-items: center; justify-content: center; gap: 14px;
  }
  .brand-dot {
    width: 40px; height: 40px; border-radius: 50%;
    background: var(--foil);
  }
  .brand-name {
    font-size: 44px; font-weight: 700; letter-spacing: 3px; color: var(--foil);
  }
  .front__title {
    position: absolute; left: 0; right: 0; top: 214px;
    text-align: center; font-size: 17px; letter-spacing: 1px; text-transform: uppercase;
  }
  /* Back */
  .card--back { background: var(--card-back); }
  .back__brand {
    position: absolute; left: 36px; top: 118px; width: 200px;
  }
  .back__mark { display: flex; align-items: center; gap: 10px; }
  .back__mark .brand-dot { width: 28px; height: 28px; }
  .back__mark .brand-name { font-size: 32px; letter-spacing: 2px; }
  .back__tagline {
    margin-top: 22px; font-size: 11px; line-height: 1.45; text-transform: uppercase; letter-spacing: 0.5px;
  }
  .back__details { position: absolute; left: 262px; top: 44px; right: 28px; }
  .person__name { font-size: 19px; letter-spacing: 1.5px; text-transform: uppercase; }
  .person__role { font-size: 10px; letter-spacing: 1px; text-transform: uppercase; margin-top: 3px; }
  .contact-list {
    list-style: none; margin-top: 30px; font-size: 11px; line-height: 1.55;
  }
  .office { margin-top: 30px; }
  .office__name { font-size: 13px; text-transform: uppercase; letter-spacing: 0.5px; }
  .office__address { font-size: 10px; margin-top: 4px; }
</style>
</head>
<body>
<main class="canvas">
  <section class="card card--front" aria-label="Business card front">
    <div class="card__frame"></div>
    <div class="front__mark">
      <span class="brand-dot"></span>
      <span class="brand-name">HBG</span>
    </div>
    <p class="front__title">HBG Construction Services</p>
  </section>

  <section class="card card--back" aria-label="Business card back">
    <div class="back__brand">
      <div class="back__mark">
        <span class="brand-dot"></span>
        <span class="brand-name">HBG</span>
      </div>
      <p class="back__tagline">Halden Build<br>Group Services</p>
    </div>
    <div class="back__details">
      <p class="person__name">Marcus Ellery</p>
      <p class="person__role">CEO &amp; Founder</p>
      <ul class="contact-list">
        <li>www.haldenbuild.com</li>
        <li>info@haldenbuild.com</li>
        <li>+1 555 014 2283</li>
        <li>+1 555 017 6490</li>
      </ul>
      <div class="office">
        <p class="office__name">HBG Construction Services</p>
        <p class="office__address">18 Alder Lane, 4th Floor, Harbor Court, Irvine, CA 926</p>
      </div>
    </div>
  </section>
</main>
</body>
</html>
```